Business card design needed

I need a business card for my new Food & Lifestyle Coaching business - "Bloomvale Food & Lifestlye Coaching"

i already have a logo and would like to have that incorporated into the business card, obviously.

i would like a design that says "fresh" and "funky" - my target market is female, aged 20-45 so i want something that will stand out to them when they see it.

My "Company Colour" is Apple Green
Updates

Thankyou to everyone who has submitted a design for my project. At this stage i have quite a large number of designs to chose from and with only a short time until my project closes i am focusing now on chosing from those i have already shortlisted so am unfortunately not considering any new desings.

Thankyou again for your interest in my project.

Target Market(s)

Female, Health Conscious (or looking to improve their health/lifestyle), aged between 20-45

Industry/Entity Type

Business

Contact Information for Business Card

Tamsin Corley
Ph: 0417382946
Email: eatwell@marovex.com

Requirements
Must have
• Must include my existing Logo
Nice to have
• Would be nice to incoirporate and appointment card on the back

```html
<!DOCTYPE html>
<html lang="en">
<head>
<meta charset="utf-8">
<title>Bloomvale Food &amp; Lifestlye Coaching – Business Card</title>
<link rel="stylesheet" href="https://fonts.googleapis.com/css2?family=Questrial&display=swap">
<style>
  :root {
    --apple-green: #7cb82f;
    --apple-green-deep: #5f9a1f;
    --apple-green-soft: #a6d160;
    --ink: #2b2b2b;
    --muted: #6b6b6b;
    --card: #ffffff;
    --card-edge: #ececec;
    --backdrop: #e9ebe6;
  }
  * { box-sizing: border-box; margin: 0; padding: 0; }
  html, body {
    width: 1200px; height: 900px; overflow: hidden;
    background: var(--backdrop);
    font-family: "Questrial", "Century Gothic", sans-serif;
  }
  .sheet {
    position: relative; width: 1200px; height: 900px;
  }
  .card {
    position: absolute; left: 280px;
    width: 640px; height: 366px;
    border-radius: 24px;
    background: linear-gradient(160deg, var(--card) 0%, #f6f6f6 100%);
    box-shadow: 0 10px 30px rgba(0,0,0,0.18), 0 0 0 1px var(--card-edge);
    overflow: hidden;
  }
  .card--front { top: 60px; }
  .card--back { top: 470px; }

  .illustration {
    position: absolute;
    border-radius: 48% 52% 46% 54% / 55% 45% 55% 45%;
    background: radial-gradient(ellipse at 40% 45%, var(--apple-green-soft) 0%, var(--apple-green) 55%, var(--apple-green-deep) 100%);
    opacity: 0.92;
  }
  .card--front .illustration { left: -60px; top: 40px; width: 390px; height: 340px; }
  .card--back .illustration { right: -50px; top: -30px; width: 380px; height: 330px; }

  .brand { position: absolute; }
  .brand__row { display: flex; align-items: center; gap: 10px; }
  .brand__dot {
    width: 18px; height: 18px; border-radius: 50%;
    background: var(--apple-green);
  }
  .brand__name {
    color: var(--ink); font-size: 46px; line-height: 1; letter-spacing: 0.5px;
  }
  .brand__tagline {
    margin-top: 6px; margin-left: 28px;
    color: var(--muted); font-size: 13px; letter-spacing: 0.3px;
  }
  .card--front .brand { right: 46px; top: 138px; }
  .card--back .brand { left: 34px; top: 34px; }
  .card--back .brand__name { font-size: 40px; }
  .card--back .brand__tagline { font-size: 12px; }

  .contact {
    position: absolute; left: 40px; top: 190px;
    color: var(--apple-green);
  }
  .contact__name { font-size: 24px; letter-spacing: 1px; }
  .contact__list {
    list-style: none; margin-top: 30px;
    border-left: 1px solid var(--apple-green-soft);
    padding-left: 22px;
  }
  .contact__item {
    display: flex; align-items: center; gap: 12px;
    font-size: 19px; letter-spacing: 0.8px; line-height: 1;
  }
  .contact__item + .contact__item { margin-top: 22px; }
  .contact__icon { width: 18px; height: 18px; flex: none; }
</style>
</head>
<body>
<main class="sheet">
  <section class="card card--front" aria-label="Card front">
    <div class="illustration" role="img" aria-label="Large green leaf-and-butterfly illustration"></div>
    <div class="brand">
      <div class="brand__row">
        <span class="brand__dot"></span>
        <span class="brand__name">Bloomvale</span>
      </div>
      <p class="brand__tagline">Food &amp; Lifestlye Coaching</p>
    </div>
  </section>

  <section class="card card--back" aria-label="Card back">
    <div class="illustration" role="img" aria-label="Large green leaf-and-butterfly illustration"></div>
    <div class="brand">
      <div class="brand__row">
        <span class="brand__dot"></span>
        <span class="brand__name">Bloomvale</span>
      </div>
      <p class="brand__tagline">Food &amp; Lifestlye Coaching</p>
    </div>
    <div class="contact">
      <p class="contact__name">Tamsin Corley</p>
      <ul class="contact__list">
        <li class="contact__item">
          <svg class="contact__icon" viewBox="0 0 18 18" aria-hidden="true">
            <rect x="5" y="1.5" width="8" height="15" rx="1.6" fill="none" stroke="currentColor" stroke-width="1.6"/>
            <line x1="7.5" y1="13.5" x2="10.5" y2="13.5" stroke="currentColor" stroke-width="1.4"/>
          </svg>
          <span>0417382946</span>
        </li>
        <li class="contact__item">
          <svg class="contact__icon" viewBox="0 0 18 18" aria-hidden="true">
            <text x="9" y="14.5" text-anchor="middle" font-size="17" fill="currentColor" font-family="Questrial, sans-serif">@</text>
          </svg>
          <span>eatwell@marovex.com</span>
        </li>
      </ul>
    </div>
  </section>
</main>
</body>
</html>
```